Design a Chart Graphic that can be animated in video

We are looking for a clean and professional chart graphic that can be used on our website and edited to come alive in a video animation. The chart is to demonstrate that our product was proven to work in a clinical study. The chart title is Clinically Proven to Improve Sleep Quality. The x axis starts at "placebo" and ends at "tova calm" the placebo starts at 2% and the tova calm is 29% - the chart would show the rise from 2% to 29% in a dramatic way. The y axis would go from 0 - 30 %. There would be some sort of arrow to demonstrate the growth. Please see drawing for more clarity.

Target Market(s)

This is a study on SLEEP, the target market is sleep deprived men and women between the ages of 35-55.

Font styles to use
Sans Serif

Colors
0456a4
85abd2
85acd3
cedeed
ffffff
f04a50
fbed22

Requirements
Must have
• The chart must be delivered in a vector and styled in a way that can be animated by our video team. We are open to either flat or 3-D styles. The chart will be used on website and in video. It needs to look clean and professional, not funny or cartoonish. The color pallet needs to match www.itovacalm.com
• Please deliver vector, JPEG and PNG of the chart with and without a title.
Nice to have
• Fresh ideas to how to represent the chart in the most compelling way
Should not have
• Cartoons, gimmicky, colors other than those that match our website.

```html
<!DOCTYPE html>
<html lang="en">
<head>
<meta charset="utf-8">
<title>Clinically Proven to Improve Sleep Quality</title>
<link href="https://fonts.googleapis.com/css2?family=Montserrat:wght@300;400;700;800&display=swap" rel="stylesheet">
<style>
  :root {
    --night: #0f0d22;
    --white: #ffffff;
    --ice: #cedeed;
    --sky: #85abd2;
    --brand-blue: #0456a4;
    --dusk: #8a5a8a;
    --coral: #f04a50;
    --grid: rgba(255, 255, 255, 0.35);
    --star: rgba(255, 255, 255, 0.55);
  }
  html, body {
    margin: 0;
    padding: 0;
    overflow: hidden;
    background: var(--night);
  }
  .chart-card {
    position: relative;
    width: 1200px;
    height: 985px;
    background: var(--night);
    overflow: hidden;
    font-family: "Montserrat", Arial, sans-serif;
    color: var(--white);
  }
  .chart-title {
    position: absolute;
    top: 100px;
    left: 0;
    width: 1300px;
    margin: 0;
    text-align: center;
    font-weight: 700;
    line-height: 1;
    letter-spacing: -0.5px;
  }
  .chart-title .kicker {
    display: block;
    font-size: 33px;
  }
  .chart-title .headline {
    display: block;
    margin-top: 12px;
    font-size: 47px;
    font-weight: 800;
  }
  .chart-graphic {
    position: absolute;
    inset: 0;
  }
  .axis-label {
    fill: var(--white);
    font-family: "Montserrat", Arial, sans-serif;
    font-weight: 300;
    font-size: 23px;
  }
  .axis-line {
    stroke: var(--white);
    stroke-width: 1.5;
    fill: none;
  }
  .grid-line {
    stroke: var(--grid);
    stroke-width: 1;
    stroke-dasharray: 2 3;
  }
  .star { fill: var(--star); }
</style>
</head>
<body>
<main class="chart-card">
  <h1 class="chart-title">
    <span class="kicker">CLINICALLY PROVEN TO IMPROVE</span>
    <span class="headline">SLEEP QUALITY</span>
  </h1>

  <svg class="chart-graphic" width="1200" height="985" viewBox="0 0 1200 985" aria-label="Sleep quality improvement: placebo 2%, Tova Calm 29%">
    <defs>
      <linearGradient id="growth-fill" x1="0" y1="282" x2="0" y2="815" gradientUnits="userSpaceOnUse">
        <stop offset="0" stop-color="var(--white)"/>
        <stop offset="0.22" stop-color="var(--sky)"/>
        <stop offset="0.48" stop-color="#3d72b8"/>
        <stop offset="0.66" stop-color="var(--brand-blue)"/>
        <stop offset="0.8" stop-color="var(--dusk)"/>
        <stop offset="1" stop-color="var(--coral)"/>
      </linearGradient>
      <filter id="star-glow" x="-2" y="-2" width="5" height="5">
        <feGaussianBlur stdDeviation="1.2"/>
      </filter>
    </defs>

    <g class="stars" filter="url(#star-glow)">
      <circle class="star" cx="499" cy="55" r="2.4"/>
      <circle class="star" cx="172" cy="107" r="2.4"/>
      <circle class="star" cx="349" cy="104" r="2.4"/>
      <circle class="star" cx="769" cy="106" r="2.4"/>
      <circle class="star" cx="1135" cy="105" r="2.4"/>
      <circle class="star" cx="331" cy="230" r="2.4"/>
      <circle class="star" cx="670" cy="214" r="2.4"/>
      <circle class="star" cx="938" cy="202" r="2.4"/>
      <circle class="star" cx="114" cy="329" r="2.4"/>
      <circle class="star" cx="1118" cy="411" r="2.4"/>
      <circle class="star" cx="393" cy="465" r="2.4"/>
      <circle class="star" cx="673" cy="468" r="2.4"/>
      <circle class="star" cx="143" cy="521" r="2.4"/>
      <circle class="star" cx="290" cy="729" r="2.4"/>
      <circle class="star" cx="815" cy="891" r="2.4"/>
    </g>

    <g class="grid">
      <line class="grid-line" x1="217" y1="282" x2="995" y2="282"/>
      <line class="grid-line" x1="217" y1="548" x2="995" y2="548"/>
    </g>

    <path class="growth-area" fill="url(#growth-fill)"
          d="M217,755 C520,700 800,570 995,282 L995,815 L217,815 Z"/>

    <g class="axes">
      <polyline class="axis-line" points="217,815 217,229"/>
      <polyline class="axis-line" points="208,238 217,229 226,238"/>
      <polyline class="axis-line" points="217,815 1085,815"/>
    </g>

    <g class="y-labels">
      <text class="axis-label" x="183" y="290" text-anchor="end">30%</text>
      <text class="axis-label" x="183" y="556" text-anchor="end">15%</text>
      <text class="axis-label" x="183" y="823" text-anchor="end">0%</text>
    </g>

    <g class="x-labels">
      <text class="axis-label" x="217" y="849">Placebo</text>
      <text class="axis-label" x="1071" y="849" text-anchor="end">Tova Calm</text>
    </g>
  </svg>
</main>
</body>
</html>
```